Environmental Company Website
Kelvro Remediation website
Project: Environmental Company Website
Environmental Company Website - Environment
Creative Brief
Environment
www.kelvroremediation.example
We are an environmental cleanup/spill response company. We service Industrial and Municiple customers. Most of our work revolves around gas/petroleum spills or tank cleaning. We need to keep a very professional, emergency response image. We are not so different than a fire department in our emergency nature. We sell spill supplies to our customers, but we will not sell from our website.
Dislike busy, clumsy, long page websites. Looking for a one page length website (if possible). No scrolling needed to view the pages unless the content demands it. The home page fills the screen, but doesn't go down below the bottom of the window. The nav bar could be on the top or left, whatever best compliments the page.
Elegant
Black / Gray / White/ Blue (see logo)
Yellow
Your choice, we're open to ideas
Arial, Verdana
top
www.lorptank.example
http://www.mavulonsite.example/
http://www.wandertidebreaks.example/
Additional websites we like: http://www.hollisquay-horology.example/en2/ http://www.pinmoorcatch.example/ http://www.oakventhomefit.example/ http://tamworkbuilders.example/ http://www.quennabay.example/ourcatch/

```html
<!DOCTYPE html>
<html lang="en">
<head>
<meta charset="utf-8">
<title>Kelvro Remediation, LLC</title>
<link rel="stylesheet" href="https://fonts.googleapis.com/css2?family=Arimo:wght@400;700&display=swap">
<style>
  :root {
    --white: #ffffff;
    --ink: #1d2a33;
    --grey: #8a969d;
    --nav-grey: #9aa6ad;
    --nav-active: #1f7fc0;
    --blue: #1c6fb0;
    --deep: #0c1c27;
    --teal: #1d4a5c;
    --yellow: #f2c511;
    --link: #b9c8d1;
  }
  * { box-sizing: border-box; margin: 0; padding: 0; }
  html, body { width: 1200px; height: 566px; overflow: hidden; }
  body { font-family: "Arimo", Arial, sans-serif; background: var(--white); position: relative; }

  .site-header { position: absolute; left: 0; top: 0; width: 1200px; height: 92px; background: var(--white); }
  .brand { position: absolute; left: 72px; top: 24px; display: flex; align-items: center; gap: 10px; }
  .brand-mark { width: 22px; height: 22px; background: var(--blue); }
  .brand-name { font-size: 20px; font-weight: 700; color: var(--ink); }

  .hotline { position: absolute; right: 190px; top: 8px; text-align: right; }
  .hotline-call { font-size: 15px; color: var(--grey); }
  .hotline-call strong { color: var(--ink); font-size: 17px; }
  .hotline-number { font-size: 26px; font-weight: 700; color: var(--blue); margin-left: 8px; }
  .hotline-email { font-size: 9px; color: var(--blue); margin-top: -2px; }

  .main-nav { position: absolute; left: 528px; top: 62px; display: flex; gap: 2px; }
  .main-nav a { display: block; height: 30px; line-height: 30px; padding: 0 14px; font-size: 11px;
    color: var(--white); text-decoration: none; background: var(--nav-grey); }
  .main-nav a.is-active { background: var(--nav-active); }

  .stage { position: absolute; left: 0; top: 92px; width: 1200px; height: 408px;
    background: radial-gradient(ellipse at 50% 40%, var(--teal), var(--deep) 75%); }

  .hero { position: absolute; left: 173px; top: 6px; width: 652px; height: 398px; overflow: hidden; }
  .hero-photo { position: absolute; inset: 0;
    background: radial-gradient(ellipse at 62% 45%, #3f5866 0%, #1e2f39 50%, #0d171e 100%); }
  .hero-copy { position: absolute; left: 29px; top: 84px; width: 300px; color: var(--white); }
  .hero-title { font-size: 22px; font-weight: 700; letter-spacing: -0.6px; white-space: nowrap; }
  .hero-sub { font-size: 18px; line-height: 22px; margin-top: 8px; }
  .hero-sub .accent { color: var(--yellow); }
  .hero-list { list-style: none; margin-top: 22px; font-size: 12px; line-height: 19px; }
  .hero-list li { position: relative; padding-left: 18px; }
  .hero-list li::before { content: ""; position: absolute; left: 2px; top: 7px; width: 6px; height: 6px;
    border-radius: 50%; background: var(--white); }

  .services { position: absolute; left: 830px; top: 6px; width: 190px; }
  .service-tile { position: relative; height: 126px; margin-bottom: 10px; border: 2px solid #cfd8dd; overflow: hidden; }
  .service-photo { position: absolute; inset: 0; }
  .service-photo.haz { background: linear-gradient(160deg, #6f8594, #3a4b56 60%, #c7ccc9); }
  .service-photo.drum { background: linear-gradient(160deg, #8e9aa0, #4d5d64 55%, #a5a068); }
  .service-photo.tank { background: linear-gradient(160deg, #5b7381, #2c3e48 60%, #7d6e5a); }
  .service-label { position: absolute; left: 0; right: 0; bottom: 0; height: 24px; line-height: 24px;
    text-align: center; font-size: 13px; color: var(--white); background: rgba(10, 22, 30, .72); }

  .site-footer { position: absolute; left: 0; top: 500px; width: 1200px; height: 66px; background: var(--deep); }
  .footer-mark { position: absolute; left: 182px; top: 17px; width: 22px; height: 22px; background: var(--blue); }
  .footer-nav { position: absolute; left: 222px; top: 17px; font-size: 11px; color: var(--link); }
  .footer-nav a { color: var(--link); text-decoration: none; }
  .footer-nav .sep { margin: 0 6px; }
  .footer-copy { position: absolute; left: 222px; top: 38px; font-size: 9px; color: var(--grey); }
  .follow { position: absolute; left: 930px; top: 17px; display: flex; align-items: center; gap: 5px;
    font-size: 10px; color: var(--grey); }
  .follow span.dot { width: 15px; height: 15px; border-radius: 3px; background: var(--blue); }
  .follow span.dot.alt { background: #3aa3dc; }
  .follow span.dot.feed { background: #e0892a; }
</style>
</head>
<body>
  <header class="site-header">
    <div class="brand">
      <span class="brand-mark"></span>
      <span class="brand-name">Kelvro Remediation, LLC</span>
    </div>
    <div class="hotline">
      <div class="hotline-call">Call <strong>24 HOURS</strong> Response! <span class="hotline-number">410-555-0147</span></div>
      <div class="hotline-email">email: info@kelvroremediation.example</div>
    </div>
    <nav class="main-nav">
      <a href="#" class="is-active">HOME</a>
      <a href="#">ABOUT US</a>
      <a href="#">SERVICES</a>
      <a href="#">EQUIPMENT</a>
      <a href="#">GALLERY</a>
      <a href="#">CONTACT</a>
    </nav>
  </header>

  <main class="stage">
    <section class="hero">
      <div class="hero-photo" role="img" aria-label="Worker in a yellow protective suit pressure-washing the inside of an industrial tank"></div>
      <div class="hero-copy">
        <h1 class="hero-title">We offer complete Cleanup</h1>
        <p class="hero-sub"><span class="accent">and</span> isposal for<br>Accident Scenes and<br>Industrial Spills and<br>Accidents</p>
        <ul class="hero-list">
          <li>Drum Sales &amp; Disposal</li>
          <li>Haz Disposal</li>
          <li>Large inventory of Sorbents, Pads,<br>Sta, Dil Soil Samples</li>
          <li>Underground Tank Removal</li>
        </ul>
      </div>
    </section>

    <aside class="services">
      <div class="service-tile">
        <div class="service-photo haz" role="img" aria-label="Crew loading hazardous waste containers onto a truck"></div>
        <div class="service-label">Haz Disposal</div>
      </div>
      <div class="service-tile">
        <div class="service-photo drum" role="img" aria-label="Rows of steel drums staged for disposal"></div>
        <div class="service-label">Drum Sales &amp; Disposal</div>
      </div>
      <div class="service-tile">
        <div class="service-photo tank" role="img" aria-label="Excavated underground storage tank being lifted out"></div>
        <div class="service-label">Underground Tank Removal</div>
      </div>
    </aside>
  </main>

  <footer class="site-footer">
    <span class="footer-mark"></span>
    <nav class="footer-nav">
      <a href="#">Home</a><span class="sep">|</span><a href="#">About Us</a><span class="sep">|</span><a href="#">Services</a><span class="sep">|</span><a href="#">Equipment</a><span class="sep">|</span><a href="#">Gallery</a><span class="sep">|</span><a href="#">Contact</a>
    </nav>
    <p class="footer-copy">© 2013 kelvroremediation.example All Rights Reserved</p>
    <div class="follow">Follow us on <span class="dot"></span><span class="dot alt"></span><span class="dot feed"></span></div>
  </footer>
</body>
</html>
```